Business card design for Tarvello Studios, and Event & Entertainment business

The business card design is for a new business venture, Tarvello Studios. This company offers Event management, entertainment management and also Latin dance tuition. We currently run Latin dance festivals in Australia & also teach street Latin. This business card is for the director, Wren Hollis. The Logo has already been designed. So, I need the new design to incorporate and go with the existing Logo.

The look I like is clean, simple & elegant but I also want it to be sexy. Elegant, but not corporate. Clean & simple but not boring :-)

If you want to add another design element as well as using the Logo, please use something with movement. I like ripples or swirls for example.

I would also like to have part of the card embossed or Spot UV pressed so I would like some part of the design to have texture.

Text for the Cards is as follows;

Tarvello Studios ( Logo attached )

Wren Hollis

EVENTS & ENTERTAINMENT MANAGEMENT

m: 0487 552 031
e: wren@tarvellostudios.com.au
f Tarvello Studios

www.tarvellostudios.com.au

Please try portrait layout.

Thanks, Wren
Updates

Hello Designers, Thank you to all of you who have submitted designs for Tarvello Studios. I will make up my mind now from what I have already been sent. Very close to making a decision :-) Thank you, Wren

Target Market(s)

Adults, 18 - 60 age group. People who are active. People interested in different cultures. People who like to travel. Please who like to have fun. People who are passionate about Latin dance.

Industry/Entity Type

Entertainment

Font styles to use
Sans Serif
Script

Colors
9bcb3c
ec1f27
ffffff

Requirements
Must have
• Logo + All text listed in brief
Nice to have
• An extra design feature or background image that could be embossed or spot uv pressed to add texture & flare.

```html
<!DOCTYPE html>
<html lang="en">
<head>
<meta charset="utf-8">
<title>Tarvello Studios — Business Card</title>
<link rel="stylesheet" href="https://fonts.googleapis.com/css2?family=Open+Sans:wght@400;600&display=swap">
<style>
  :root {
    --backdrop: #232323;
    --card: #ffffff;
    --ink: #2e2e2e;
    --accent-red: #d9241f;
    --accent-green: #9bcb3c;
    --swirl: #ececec;
    --band-text: #ffffff;
  }
  * { box-sizing: border-box; margin: 0; padding: 0; }
  html, body {
    width: 1200px;
    height: 1100px;
    overflow: hidden;
    background: var(--backdrop);
    font-family: "Open Sans", Arial, sans-serif;
    color: var(--ink);
  }
  .stage {
    position: relative;
    width: 1200px;
    height: 1100px;
  }
  .card {
    position: absolute;
    top: 235px;
    width: 380px;
    height: 630px;
    background: var(--card);
    overflow: hidden;
  }
  .card--front { left: 175px; }
  .card--back  { left: 645px; }

  .texture-swirl {
    position: absolute;
    left: 0;
    bottom: 0;
    width: 380px;
    height: 260px;
  }
  .texture-swirl path {
    fill: none;
    stroke: var(--swirl);
    stroke-width: 2;
  }

  .wordmark {
    position: absolute;
    left: 0;
    right: 0;
    display: flex;
    align-items: center;
    justify-content: center;
    gap: 10px;
  }
  .wordmark__dot {
    width: 14px;
    height: 14px;
    border-radius: 50%;
    background: var(--accent-red);
    flex: none;
  }
  .wordmark__name {
    font-weight: 600;
    font-size: 30px;
    letter-spacing: 0.5px;
    color: var(--ink);
    white-space: nowrap;
  }
  .card--front .wordmark { top: 290px; }
  .card--back .wordmark { top: 110px; }

  .director {
    position: absolute;
    top: 196px;
    left: 0;
    right: 0;
    text-align: center;
    font-size: 20px;
    font-weight: 600;
    letter-spacing: 0.3px;
    color: var(--ink);
  }

  .tagline {
    position: absolute;
    top: 252px;
    left: 0;
    right: 0;
    text-align: center;
    font-size: 19px;
    line-height: 1.35;
    letter-spacing: 0.3px;
    text-transform: uppercase;
    color: var(--ink);
  }

  .contacts {
    position: absolute;
    top: 392px;
    left: 0;
    right: 0;
    list-style: none;
    text-align: center;
    font-size: 18px;
    line-height: 1.4;
    color: var(--ink);
  }
  .contacts__label { color: var(--accent-red); }

  .web-band {
    position: absolute;
    left: 0;
    right: 0;
    bottom: 0;
    height: 70px;
    background: var(--accent-red);
    color: var(--band-text);
    display: flex;
    align-items: center;
    justify-content: center;
    font-size: 19px;
    letter-spacing: 0.2px;
  }
</style>
</head>
<body>
  <main class="stage">
    <section class="card card--front" aria-label="Card front">
      <svg class="texture-swirl" viewBox="0 0 380 260" aria-hidden="true">
        <path d="M-20 200 C 60 120, 160 260, 240 170 S 360 90, 400 150"/>
        <path d="M-20 225 C 70 145, 170 280, 250 195 S 365 115, 400 175"/>
        <path d="M-20 250 C 80 170, 180 300, 260 220 S 370 140, 400 200"/>
      </svg>
      <div class="wordmark">
        <span class="wordmark__dot"></span>
        <span class="wordmark__name">Tarvello Studios</span>
      </div>
    </section>

    <section class="card card--back" aria-label="Card back">
      <div class="wordmark">
        <span class="wordmark__dot"></span>
        <span class="wordmark__name">Tarvello Studios</span>
      </div>

      <p class="director">Wren Hollis</p>

      <p class="tagline">Events &amp; Entertainment<br>Management</p>

      <ul class="contacts">
        <li><span class="contacts__label">m:</span> 0487 552 031</li>
        <li><span class="contacts__label">e:</span> wren@tarvellostudios.com.au</li>
        <li><span class="contacts__label">f:</span> Tarvello Studios</li>
      </ul>

      <div class="web-band">www.tarvellostudios.com.au</div>
    </section>
  </main>
</body>
</html>
```